Infographic Design for Aluminium Can Recycling

We require a neat design that can be integrated into print advertising for a 'cash for cans' recycling promotion and also scaled back for Facebook promotion. The promotion is aimed at kids/families. Needs to be fresh and colourful - but also appealing to children. The flyer is to be designed at A5 size and also at FB post sizing. You can just submit the one design in A5 to win, with the knowledge that you will need to redesign slightly later to suit FB post size.

The design needs to contain as much of the following as possible.

- The best thing is - Aluminium is 100% recyclable FOREVER
- If you recycled just one can everyday for a week, you'd save enough energy to watch TV straight for 21 hours - thats an entire season of XXX
- 105,784 cans are recycled every minute
- it takes the same amount of energy to make 1 new can as it does to recycle 20
- a recycled can is back on the shelf in 60 days
-2/3 of the aluminium ever produced is still in use today

Please keep colours muted - not bright
Please do not present anything like the 'Tidy Loop' lie attached. This is far too busy.
I have attached the original flyer for information only (see below for what to and what NOT to include)
I've attached some cute graphics I think kids and adults will find appealing. Design something similar. The prize to be won is an electric scooter - perhaps they could be riding this.

They are giving away an electric Scooter (not Bike)

Please use Pellbrook Alloy Traders and LOGO

Please provide address and details of event as per flyer

Please leave out the following text:
HEY KIDS
WIN THIS BIKE
FIND US ON FB
LUCKY DOOR PRIZE + SAUSAGE SIZZLE
WE PAY CASH FOR CANS
Collect as many aluminium cans as you can and bring them to our can day and get paid for cash
Do not include the can man graphic

Please have information:
Event location
Win an Electric Scooter
Turn in your CANS for CASH

Great - can't wait to see what you creative geniuses come back with!!
Updates

None of these designs matched the brief. Im actually not sure what to do now?

Target Market(s)

Males 35+

Industry/Entity Type

Advertising

Font styles to use
Sans Serif

Colors
5c5c5c
0555a3
3276b5
b1b1b1
faa54b
fbf289
33a6d7
f04a50

Requirements
Must have
• Please read brief
Nice to have
• Please see brief
Should not have
• Please see brief

```html
<!DOCTYPE html>
<html lang="en">
<head>
<meta charset="utf-8">
<title>Turn In Your Cans For Cash – Pellbrook Alloy Traders</title>
<link rel="stylesheet" href="https://fonts.googleapis.com/css2?family=Dosis:wght@500;600;700&family=Open+Sans:wght@400;600;700&family=Caveat:wght@500&display=swap">
<style>
  :root {
    --paper: #f3f1e7;
    --paper-edge: #dedbc9;
    --green: #4f8a5b;
    --green-dark: #3f7a52;
    --green-fill: #7dae4b;
    --green-light: #8cbf4a;
    --red: #d9523d;
    --blue: #2f7ba6;
    --blue-dark: #1f6a95;
    --orange: #f6ae57;
    --orange-box: #fbb45e;
    --cream: #f8efaf;
    --text: #3c3c3c;
    --grey: #b1b1b1;
    --yellow: #f9d56c;
  }
  * { margin: 0; padding: 0; box-sizing: border-box; }
  html, body { width: 1200px; height: 855px; overflow: hidden; }
  body {
    background: radial-gradient(ellipse at 50% 45%, #fbfaf4 0%, var(--paper) 55%, var(--paper-edge) 100%);
    font-family: "Open Sans", Arial, sans-serif;
    color: var(--text);
    position: relative;
  }
  .connectors { position: absolute; inset: 0; }
  .abs { position: absolute; }

  .fact-text { font-size: 19px; line-height: 1.4; }
  .big-number { font-family: "Open Sans", sans-serif; font-weight: 700; line-height: 1; }

  /* Fact: recyclable forever */
  .fact-forever .badge { left: 48px; top: 62px; width: 64px; height: 62px; border-radius: 8px; background: var(--green); }
  .fact-forever .big-number { left: 126px; top: 58px; font-size: 64px; color: var(--green); }
  .fact-forever .fact-text { left: 314px; top: 70px; }
  .fact-forever .forever { color: var(--green-light); font-weight: 700; }
  .note { left: 542px; top: 64px; font-family: "Caveat", cursive; font-size: 20px; color: var(--text); }

  /* Fact: cans per minute */
  .fact-minute .icon { left: 52px; top: 192px; }
  .fact-minute .big-number { left: 126px; top: 198px; font-size: 56px; color: var(--red); }
  .fact-minute .unit { left: 354px; top: 220px; font-size: 30px; font-weight: 700; color: var(--red); }
  .fact-minute .fact-text { left: 130px; top: 256px; }

  /* Fact: back on shelf */
  .fact-shelf .fact-text { left: 55px; top: 370px; }
  .fact-shelf .big-number { left: 200px; top: 366px; font-size: 60px; color: var(--green-dark); }
  .fact-shelf .unit { left: 204px; top: 424px; font-size: 27px; font-weight: 700; color: var(--green-light); }
  .fact-shelf .icon { left: 286px; top: 366px; }

  /* Fact: TV */
  .fact-tv .fact-text { left: 868px; top: 66px; font-size: 19px; line-height: 1.42; }
  .fact-tv .icon { left: 1030px; top: 70px; }
  .fact-tv .big-number { left: 1032px; top: 170px; font-size: 68px; color: var(--blue-dark); }
  .fact-tv .unit { left: 1032px; top: 234px; font-size: 29px; font-weight: 600; color: var(--blue-dark); }

  /* Fact: still in use */
  .fact-use .cans { left: 835px; top: 330px; width: 165px; height: 92px; background: linear-gradient(90deg, #f5c66b 0 33%, #f5d98a 33% 66%, #c6c6c6 66% 100%); opacity: .9; }
  .fact-use .big-number { left: 1008px; top: 342px; font-size: 68px; }
  .fact-use .two { color: var(--orange); }
  .fact-use .three { color: var(--grey); }
  .fact-use .fact-text { left: 837px; top: 434px; }

  /* Headline roundel */
  .roundel { left: 410px; top: 128px; width: 400px; height: 400px; }
  .headline {
    left: 440px; top: 212px; width: 340px; text-align: center;
    font-family: "Dosis", sans-serif; font-weight: 600; font-size: 58px; line-height: 1.1;
    letter-spacing: 2px; color: var(--cream); text-transform: uppercase;
  }

  /* People */
  .person { width: 114px; height: 114px; border-radius: 50%; top: 604px; }
  .person-boy { left: 98px; background: radial-gradient(circle at 50% 60%, #f2c9a0 0 34%, #8fbf4e 35%); }
  .person-girl { left: 242px; background: radial-gradient(circle at 50% 60%, #f2c9a0 0 34%, #e2584a 35%); }
  .person-man { left: 824px; background: radial-gradient(circle at 50% 60%, #f2c9a0 0 34%, #2f7ba6 35%); }
  .person-woman { left: 972px; background: radial-gradient(circle at 50% 60%, #f6e2b0 0 34%, #f8c55a 35%); }

  /* Event details */
  .pointer { left: 572px; top: 530px; }
  .event {
    left: 397px; top: 590px; width: 410px; height: 138px;
    background: var(--orange-box); border-radius: 6px;
    text-align: center; padding-top: 14px;
    font-size: 19px; line-height: 1.4; color: #2e2e2e;
  }
  .event b { font-weight: 700; }

  .prize {
    left: 242px; top: 757px; width: 728px;
    font-family: "Dosis", sans-serif; font-weight: 700; font-size: 65px;
    letter-spacing: 0.5px; color: var(--red); text-transform: uppercase; line-height: 1;
    white-space: nowrap;
  }

  .brand { left: 996px; top: 748px; width: 120px; text-align: center; }
  .brand-dot { width: 40px; height: 40px; border-radius: 50%; background: var(--blue-dark); margin: 0 auto 4px; }
  .brand-name { font-family: "Open Sans", sans-serif; font-weight: 700; font-size: 11px; line-height: 1.15; color: var(--blue-dark); text-transform: uppercase; }
</style>
</head>
<body>

<svg class="connectors" width="1200" height="855" aria-hidden="true">
  <polyline points="48,138 500,138 500,185" fill="none" stroke="var(--green)" stroke-width="4"/>
  <line x1="48" y1="291" x2="420" y2="291" stroke="var(--red)" stroke-width="4"/>
  <line x1="48" y1="468" x2="460" y2="468" stroke="var(--green)" stroke-width="4"/>
  <line x1="800" y1="287" x2="1125" y2="287" stroke="var(--blue)" stroke-width="4"/>
  <line x1="700" y1="502" x2="1125" y2="502" stroke="var(--orange)" stroke-width="4"/>
  <path d="M540 86 C 520 96, 515 108, 508 110" fill="none" stroke="#555" stroke-width="1.2" stroke-dasharray="3 3"/>
</svg>

<section class="fact fact-forever">
  <div class="abs badge" aria-hidden="true"></div>
  <div class="abs big-number">100%</div>
  <p class="abs fact-text">Aluminium is<br>recyclable <span class="forever">FOREVER</span></p>
  <span class="abs note">the best thing</span>
</section>

<section class="fact fact-minute">
  <svg class="abs icon" width="56" height="80" viewBox="0 0 56 80" aria-hidden="true">
    <rect x="2" y="0" width="52" height="8" fill="var(--red)"/>
    <rect x="2" y="72" width="52" height="8" fill="var(--red)"/>
    <path d="M8 10 H48 L30 40 L48 70 H8 L26 40 Z" fill="none" stroke="var(--red)" stroke-width="5"/>
    <path d="M14 66 L28 48 L42 66 Z" fill="var(--red)"/>
  </svg>
  <div class="abs big-number">105,784</div>
  <span class="abs unit">cans</span>
  <p class="abs fact-text">are recycled every minute</p>
</section>

<section class="fact fact-shelf">
  <p class="abs fact-text">A recycled can<br>is back on<br>the shelf in</p>
  <div class="abs big-number">60</div>
  <span class="abs unit">days</span>
  <svg class="abs icon" width="84" height="86" viewBox="0 0 84 86" aria-hidden="true">
    <rect x="4" y="10" width="76" height="72" rx="6" fill="none" stroke="var(--green-dark)" stroke-width="6"/>
    <rect x="4" y="10" width="76" height="16" fill="var(--green-dark)"/>
    <rect x="18" y="2" width="7" height="16" rx="3" fill="var(--green-dark)"/>
    <rect x="59" y="2" width="7" height="16" rx="3" fill="var(--green-dark)"/>
    <g fill="var(--green-dark)">
      <rect x="16" y="34" width="10" height="9"/><rect x="30" y="34" width="10" height="9"/><rect x="44" y="34" width="10" height="9"/><rect x="58" y="34" width="10" height="9"/>
      <rect x="16" y="48" width="10" height="9"/><rect x="30" y="48" width="10" height="9"/><rect x="44" y="48" width="10" height="9"/><rect x="58" y="48" width="10" height="9"/>
      <rect x="16" y="62" width="10" height="9"/><rect x="30" y="62" width="10" height="9"/><rect x="44" y="62" width="10" height="9"/>
    </g>
  </svg>
</section>

<section class="fact fact-tv">
  <p class="abs fact-text">If you recycled<br>just one can<br>everyday for a<br>week, you'd<br>save enough<br>energy to watch<br>TV straight for</p>
  <svg class="abs icon" width="96" height="92" viewBox="0 0 96 92" aria-hidden="true">
    <rect x="2" y="2" width="92" height="70" fill="var(--blue-dark)"/>
    <rect x="9" y="9" width="78" height="56" fill="var(--red)"/>
    <line x1="20" y1="32" x2="36" y2="18" stroke="#f6d8c8" stroke-width="4"/>
    <line x1="22" y1="42" x2="44" y2="22" stroke="#f6d8c8" stroke-width="4"/>
    <rect x="42" y="72" width="12" height="12" fill="var(--blue-dark)"/>
    <rect x="28" y="84" width="40" height="6" fill="var(--blue-dark)"/>
  </svg>
  <div class="abs big-number">21</div>
  <span class="abs unit">hours</span>
</section>

<section class="fact fact-use">
  <div class="abs cans" role="img" aria-label="Illustration of three aluminium cans, two yellow and one grey"></div>
  <div class="abs big-number"><span class="two">2</span><span class="three">/3</span></div>
  <p class="abs fact-text">of the aluminium ever<br>produced is still in use today</p>
</section>

<svg class="abs roundel" viewBox="0 0 400 400" aria-hidden="true">
  <circle cx="200" cy="200" r="198" fill="var(--orange)"/>
  <circle cx="200" cy="200" r="184" fill="var(--red)"/>
  <circle cx="200" cy="200" r="178" fill="var(--blue)"/>
  <circle cx="200" cy="200" r="172" fill="var(--green-fill)"/>
</svg>
<h1 class="abs headline">Turn in<br>your cans<br>for cash</h1>

<div class="abs person person-boy" role="img" aria-label="Illustrated boy avatar on a green circle"></div>
<div class="abs person person-girl" role="img" aria-label="Illustrated girl avatar on a red circle"></div>
<div class="abs person person-man" role="img" aria-label="Illustrated man avatar on a blue circle"></div>
<div class="abs person person-woman" role="img" aria-label="Illustrated woman avatar on a yellow circle"></div>

<svg class="abs pointer" width="72" height="72" viewBox="0 0 72 72" aria-hidden="true">
  <circle cx="36" cy="36" r="36" fill="var(--orange)"/>
  <path d="M27 18 H45 V36 H56 L36 58 L16 36 H27 Z" fill="#fbf3df"/>
</svg>

<section class="abs event">
  <p><b>WHEN:</b> Saturday 25th October</p>
  <p><b>WHERE:</b> 18 Harrow Lane Westbrook</p>
  <p><b>TIME:</b> 8am -12pm</p>
  <p><b>PHONE:</b> 0240001234 / 1300555010</p>
</section>

<h2 class="abs prize">Win an electric scooter</h2>

<div class="abs brand">
  <div class="brand-dot" aria-hidden="true"></div>
  <p class="brand-name">Pellbrook Alloy Traders</p>
</div>

</body>
</html>
```